eBook opt in for website

I write short ebooks (2500 words) to give free as an opt in. I need a cover design with block headers within the pages to highlight the specifics sections for PDF.
Book Title:
Harbor Compass Method
Sharpen Every Crew Bond Using Five Quiet Habits
I would like to see a design for the front cover that would emphasize a leader's personal growth to team.
The color that comes to mind is blue.
I do have a Brand Design and Icon if you need it.

Target Market(s)
Leaders with Team Responsibility
Industry/Entity Type
Business Consultant
Look and feel

```html
<!DOCTYPE html>
<html lang="en">
<head>
<meta charset="utf-8">
<title>Harbor Compass Method – eBook Cover</title>
<link href="https://fonts.googleapis.com/css2?family=Montserrat:wght@500;600&display=swap" rel="stylesheet">
<style>
  :root {
    --cover-blue: #417f9e;
    --spine-blue: #195f88;
    --photo-pale: #eef2f5;
    --photo-light: #d3dde5;
    --photo-mid: #a9bccb;
    --photo-deep: #4f79a6;
    --photo-floor: #c2ccd4;
    --text-white: #ffffff;
    --accent-gold: #c9a25a;
  }
  * { margin: 0; padding: 0; box-sizing: border-box; }
  html, body { width: 847px; height: 1200px; overflow: hidden; }
  body { font-family: "Montserrat", Arial, sans-serif; background: var(--cover-blue); }
  .cover {
    position: relative;
    width: 847px; height: 1200px;
    background: var(--cover-blue);
    color: var(--text-white);
    overflow: hidden;
  }
  .spine {
    position: absolute; left: 0; top: 0;
    width: 31px; height: 100%;
    background: var(--spine-blue);
  }
  .title {
    position: absolute; left: 52px; top: 30px;
    font-weight: 600;
    font-size: 76px;
    line-height: 130px;
    letter-spacing: 0.5px;
    text-transform: uppercase;
    white-space: nowrap;
  }
  .hero-image {
    position: absolute; left: 31px; top: 293px;
    width: 816px; height: 547px;
    background:
      radial-gradient(ellipse 30% 45% at 50% 8%, var(--photo-deep) 0%, rgba(79,121,166,0.55) 45%, rgba(79,121,166,0) 100%),
      radial-gradient(ellipse 55% 35% at 50% 72%, var(--photo-pale) 0%, rgba(238,242,245,0) 100%),
      linear-gradient(90deg, var(--photo-light) 0%, var(--photo-mid) 18%, var(--photo-light) 40%, var(--photo-light) 60%, var(--photo-mid) 82%, var(--photo-light) 100%),
      linear-gradient(180deg, var(--photo-light) 0%, var(--photo-light) 78%, var(--photo-floor) 100%);
    background-blend-mode: normal, normal, multiply, normal;
  }
  .subtitle {
    position: absolute; left: 52px; top: 905px;
    font-weight: 600;
    font-size: 44px;
    line-height: 63px;
    letter-spacing: -0.4px;
    white-space: nowrap;
  }
  .author {
    position: absolute; left: 50px; top: 1083px;
    font-weight: 600;
    font-size: 78px;
    line-height: 1;
    letter-spacing: -0.5px;
    text-transform: uppercase;
    white-space: nowrap;
  }
  .brand-mark {
    position: absolute; left: 656px; top: 954px;
    width: 162px; height: 162px;
    border: 2px solid var(--accent-gold);
    border-radius: 50%;
    display: flex; align-items: flex-start; justify-content: center;
    padding-top: 44px;
  }
  .brand-name {
    font-weight: 500;
    font-size: 22px;
    color: var(--accent-gold);
  }
</style>
</head>
<body>
  <main class="cover">
    <div class="spine"></div>
    <h1 class="title">Harbor Compass<br>Method</h1>
    <div class="hero-image" role="img" aria-label="Two large open hands cupped protectively over a row of business leaders and team members standing together on a reflective office surface"></div>
    <p class="subtitle">Sharpen Every Crew Bond Using<br>Five Quiet Habits</p>
    <div class="brand-mark"><span class="brand-name">Whitlock</span></div>
    <p class="author">Dana Whitlock</p>
  </main>
</body>
</html>
```